Vision, Mission and Culture Posters

We have written text paragraphs for our company vision and mission and need them made into a2 or a3 sized posters using our logo for inspiration for colour. Our company culture has 10 paragraphs and we'd like this to be a single poster of a2 or a1. Each poster should have the logo on and share common design. It's not a complex job really.

It Company

• These will be going up on our office wall so need to be clear to read from a distance and look professional but also not stodgy.

```html
<!DOCTYPE html>
<html lang="en">
<head>
<meta charset="utf-8">
<title>Bayline Parking Lets – Vision and Mission</title>
<link rel="stylesheet" href="https://fonts.googleapis.com/css2?family=Open+Sans:wght@400;700&display=swap">
<style>
  :root {
    --sky-light: #e6e8e9;
    --sky-haze: #b9bdc0;
    --skyline: #8a8f93;
    --lot-mid: #4a4d50;
    --lot-dark: #1b1c1d;
    --vision-deep: #a51d22;
    --vision-light: #d3403a;
    --mission-deep: #ec7420;
    --mission-light: #f6a25a;
    --footer-light: #f4f4f4;
    --footer-deep: #b3b3b3;
    --heading-dark: #1c1c1c;
    --text-light: #ffffff;
    --brand-yellow: #ffec00;
    --brand-ink: #111111;
  }
  * { margin: 0; padding: 0; box-sizing: border-box; }
  html, body { width: 848px; height: 1200px; overflow: hidden; background: #ffffff; }
  body { font-family: "Open Sans", Arial, sans-serif; }
  .poster { position: relative; width: 848px; height: 1200px; overflow: hidden; }

  .hero-photo {
    position: absolute; left: 0; top: 0; width: 848px; height: 480px;
    background:
      radial-gradient(ellipse 260px 90px at 545px 215px, rgba(200,202,204,0.55), rgba(120,124,128,0.25) 60%, transparent 100%),
      radial-gradient(ellipse 520px 110px at 430px 140px, rgba(255,255,255,0.35), transparent 70%),
      radial-gradient(ellipse 900px 300px at 50% 480px, rgba(0,0,0,0.55), transparent 80%),
      linear-gradient(180deg,
        var(--sky-light) 0%,
        var(--sky-haze) 14%,
        var(--skyline) 22%,
        #9da1a4 30%,
        #6c7073 38%,
        var(--lot-mid) 55%,
        #2e3032 75%,
        var(--lot-dark) 100%);
  }

  .statement { position: absolute; left: 0; width: 848px; color: var(--text-light); }
  .statement h2 { font-weight: 700; font-size: 26px; line-height: 30px; margin-bottom: 6px; }
  .statement p { font-size: 17px; line-height: 24px; text-align: justify; width: 708px; margin-left: 2px; }

  .vision {
    top: 480px; height: 142px; padding: 27px 0 0 69px;
    background: radial-gradient(ellipse at 50% 40%, var(--vision-light) 0%, var(--vision-deep) 75%);
  }
  .vision h2 { color: var(--text-light); }

  .mission {
    top: 622px; height: 258px; padding: 27px 0 0 69px;
    background: radial-gradient(ellipse at 50% 40%, var(--mission-light) 0%, var(--mission-deep) 70%);
  }
  .mission h2 { color: var(--heading-dark); }

  .brand-footer {
    position: absolute; left: 0; top: 880px; width: 848px; height: 320px;
    background: radial-gradient(ellipse at 50% 30%, var(--footer-light) 0%, var(--footer-deep) 100%);
    display: flex; align-items: center; justify-content: center; gap: 26px;
  }
  .brand-mark { width: 64px; height: 64px; background: var(--brand-yellow); }
  .brand-name { font-weight: 700; font-size: 52px; color: var(--brand-ink); letter-spacing: 0.5px; }
</style>
</head>
<body>
<main class="poster">
  <div class="hero-photo" role="img" aria-label="Photograph of a silver sports coupe on an empty rooftop car park with tyre marks, city buildings behind"></div>

  <section class="statement vision">
    <h2>Our Vision</h2>
    <p>To provide the most hassle-free parking rental service whilst giving a personal customer experience people want to tell their friends about</p>
  </section>

  <section class="statement mission">
    <h2>Our Mission</h2>
    <p>Our mission is to achieve great customer satisfaction in everything we do and offer for meeting our customers’ parking needs. We believe our path to achieving this comes through giving a simple yet thorough and friendly service to our customers without unnecessary complication. We will achieve this through using the technology available to us, continual staff training and development, regular refinement of our practices and processes along with commitment to our roles and the foundations for building our success.</p>
  </section>

  <footer class="brand-footer">
    <span class="brand-mark" aria-hidden="true"></span>
    <span class="brand-name">Bayline Parking Lets</span>
  </footer>
</main>
</body>
</html>
```